New York IT Service, Technology & Security Co.

need a new business card design for our Technology & Security Company. We are a Computer Networking Company, Security Camera Installers, Phone Systems.

Target Market(s)

Construction, Medical, Law Offices, Accounting, Retail etc.

Industry/Entity Type

Information Technology

Contact Information for Business Card

Logo is attached, colors are Blue, Red, Black. Blue for Technology & Red is for Security Cameras, Access Control, Alarm Systems

Colors
fbed22
ec1f27
0555a3
ffffff

Requirements
Must have
• Pictures or Icons for
• For Technology:
• Computer, Network, Phone System, Copier, TV, Cabling
• For Security:
• Video Surveillance, Access Control, Intercom, Fire Alarm, Burglar Alarm, Time Clock

```html
<!DOCTYPE html>
<html lang="en">
<head>
<meta charset="utf-8">
<title>Metro Line IT Service – Business Card</title>
<link href="https://fonts.googleapis.com/css2?family=Open+Sans:wght@400;600;700;800&display=swap" rel="stylesheet">
<style>
  :root {
    --blue: #0555a3;
    --red: #ec1f27;
    --yellow: #fbed22;
    --white: #ffffff;
    --paper: #f4f4f2;
    --ink: #1d1d1d;
    --grey: #555555;
    --stage: #d3d6d5;
  }
  * { margin: 0; padding: 0; box-sizing: border-box; }
  html, body {
    width: 1200px; height: 1050px; overflow: hidden;
    background: var(--stage);
    font-family: "Open Sans", Arial, sans-serif;
  }
  .card {
    position: absolute; left: 180px; width: 840px; height: 480px;
    background: var(--paper);
    box-shadow: 0 6px 18px rgba(0,0,0,0.12);
  }
  .card--front { top: 30px; border-top: 4px solid var(--blue); border-bottom: 4px solid var(--blue); }
  .card--back { top: 540px; }

  .brand {
    position: absolute; left: 40px; top: 0; width: 420px; height: 100%;
    display: flex; align-items: center; justify-content: center; gap: 12px;
  }
  .brand__mark { width: 18px; height: 18px; background: var(--red); flex: none; }
  .brand__name {
    font-weight: 800; font-size: 34px; color: var(--ink);
    letter-spacing: -0.5px; text-transform: uppercase; white-space: nowrap;
  }
  .divider {
    position: absolute; left: 490px; top: 110px; width: 3px; height: 260px;
    background: var(--blue);
  }
  .person { position: absolute; left: 530px; top: 120px; }
  .person__name { font-weight: 700; font-size: 26px; color: var(--ink); letter-spacing: 0.5px; }
  .person__role { font-size: 17px; color: var(--grey); margin-top: 2px; letter-spacing: 1px; }
  .contacts { list-style: none; margin-top: 26px; }
  .contacts li {
    display: flex; align-items: center; gap: 14px;
    font-size: 12px; color: var(--grey); line-height: 1.35;
    margin-bottom: 12px; text-transform: uppercase;
  }
  .contacts svg { width: 28px; height: 28px; flex: none; }
  .back-art { display: block; width: 840px; height: 480px; }
</style>
</head>
<body>

<section class="card card--front">
  <div class="brand">
    <span class="brand__mark"></span>
    <span class="brand__name">Metro Line IT Service</span>
  </div>
  <div class="divider"></div>
  <div class="person">
    <div class="person__name">DANA WHITFIELD</div>
    <div class="person__role">MANAGER</div>
    <ul class="contacts">
      <li>
        <svg viewBox="0 0 28 28"><circle cx="14" cy="14" r="13" fill="none" stroke="#1d1d1d" stroke-width="2"/><rect x="8" y="10" width="12" height="8" fill="none" stroke="#1d1d1d" stroke-width="1.6"/><path d="M8 10l6 5 6-5" fill="none" stroke="#1d1d1d" stroke-width="1.6"/></svg>
        <span>info@companyname.com</span>
      </li>
      <li>
        <svg viewBox="0 0 28 28"><circle cx="14" cy="14" r="13" fill="none" stroke="#1d1d1d" stroke-width="2"/><path d="M10 8c-2 2 0 7 3 10s8 5 10 3l-3-3-2 1c-2-1-4-3-5-5l1-2z" fill="#1d1d1d" transform="translate(-2 -1)"/></svg>
        <span>+00 1234 5678 9012<br>+00 1234 5678 9012</span>
      </li>
      <li>
        <svg viewBox="0 0 28 28"><circle cx="14" cy="14" r="13" fill="none" stroke="#1d1d1d" stroke-width="2"/><path d="M7 14l7-6 7 6M9 13v7h10v-7" fill="none" stroke="#1d1d1d" stroke-width="1.8"/></svg>
        <span>Your City Address<br>Street Location, NY City, USA</span>
      </li>
      <li>
        <svg viewBox="0 0 28 28"><circle cx="14" cy="14" r="13" fill="none" stroke="#1d1d1d" stroke-width="2"/><circle cx="14" cy="14" r="7" fill="none" stroke="#1d1d1d" stroke-width="1.5"/><path d="M7 14h14M14 7c-3 4-3 10 0 14M14 7c3 4 3 10 0 14" fill="none" stroke="#1d1d1d" stroke-width="1.2"/></svg>
        <span>www.companyname.com</span>
      </li>
    </ul>
  </div>
</section>

<section class="card card--back">
  <svg class="back-art" viewBox="0 0 840 480" font-family="Open Sans, Arial, sans-serif">
    <rect width="840" height="480" fill="#f4f4f2"/>
    <rect x="0" y="0" width="840" height="4" fill="#ec1f27"/>
    <polygon class="panel-security" points="0,44 560,44 300,384 0,384" fill="#ec1f27"/>
    <line x1="560" y1="44" x2="840" y2="44" stroke="#ec1f27" stroke-width="3"/>
    <polygon class="panel-technology" points="468,164 840,164 840,384 300,384" fill="#0555a3"/>
    <line x1="560" y1="44" x2="468" y2="164" stroke="#0555a3" stroke-width="3"/>
    <rect x="0" y="476" width="840" height="4" fill="#0555a3"/>

    <text x="150" y="92" fill="#ffffff" font-weight="700" font-size="20">FOR SECURITY</text>
    <g fill="#ffffff" font-size="18">
      <text x="120" y="132">•&#160;&#160;Video Surveillance</text>
      <text x="120" y="168">•&#160;&#160;Access Control</text>
      <text x="120" y="204">•&#160;&#160;Intercom</text>
      <text x="120" y="240">•&#160;&#160;Fire Alarm</text>
      <text x="120" y="276">•&#160;&#160;Burglar Alarm</text>
      <text x="120" y="312">•&#160;&#160;Time Clock</text>
    </g>

    <text x="620" y="126" fill="#0555a3" font-weight="700" font-size="20">FOR TECHNOLOGY</text>
    <g fill="#ffffff" font-size="18">
      <text x="600" y="200">•&#160;&#160;Computer</text>
      <text x="600" y="230">•&#160;&#160;Network</text>
      <text x="600" y="260">•&#160;&#160;Phone System</text>
      <text x="600" y="290">•&#160;&#160;Copier</text>
      <text x="600" y="320">•&#160;&#160;TV</text>
      <text x="600" y="350">•&#160;&#160;Cabling</text>
    </g>

    <g class="icons" fill="none" stroke="#0555a3" stroke-width="2.5">
      <path d="M548 412h36v22h-36zM556 404h20v8M556 434v10h20v-10"/>
      <path d="M646 408h44v28h-44zM662 446h12M668 436v10"/>
      <path d="M756 404h22v44h-22zM764 442h6M786 418c4 4 4 12 0 16M792 414c6 6 6 18 0 24"/>
    </g>
  </svg>
</section>

</body>
</html>
```